Shuffleboard Top graphic-Blending Several Country Flags

Hello, i am custom ordering a 12' shuffleboard for my home. My partner and I are both very proud of our heritage and i would like to incorporate our flags in the design for the top of the board, along with the USA flag, either all togerher or separating the three (USA, his flags and mine).

His nationality and country flags are Russia, Amenia and Moldova. Mine are Ireland, Italy, Germany and Hungary.

I'm envisioning either my 4 flags together on poles and his 3 flags together for two separate designs. OR, have the USA flag bleed into all of our flags in a linear design.

The design should be in a rectangle format and I can provide some estimated measurements.

Designs look the same

Friends and family

• USA flags and our nationality flags: his-Russia, Armenia, Moldova. Mine-Italy, Ireland, Germany, Hungary
• Either his flags togerher as a group in one graphic and mine in a separate graphic. OR. All of our flags combined/blender together with the USA flag

```html
<!DOCTYPE html>
<html lang="en">
<head>
<meta charset="utf-8">
<title>We Proud of Our Heritage – Shuffleboard Top</title>
<link rel="stylesheet" href="https://fonts.googleapis.com/css2?family=Days+One&display=swap">
<style>
  :root {
    --usa-red: #b22234;
    --usa-white: #ffffff;
    --usa-blue: #3c3b6e;
    --gold-light: #ffe9a8;
    --gold-mid: #d9a441;
    --gold-dark: #6b4514;
    --title-outline: #4a0c12;
    --ireland-green: #169b62;
    --ireland-orange: #ff883e;
    --italy-green: #009246;
    --italy-red: #ce2b37;
    --hungary-red: #cd2a3e;
    --hungary-green: #436f4d;
    --germany-black: #000000;
    --germany-red: #dd0000;
    --germany-gold: #ffce00;
    --armenia-red: #d90012;
    --armenia-blue: #0033a0;
    --armenia-orange: #f2a800;
    --russia-blue: #0039a6;
    --russia-red: #d52b1e;
    --moldova-blue: #0046ae;
    --moldova-yellow: #ffd200;
    --moldova-red: #cc092f;
    --emblem-gold: #c9a04a;
    --emblem-brown: #8a5a2b;
  }
  html, body {
    margin: 0;
    padding: 0;
    width: 1200px;
    height: 627px;
    overflow: hidden;
    background: var(--usa-white);
  }
  .board-top {
    display: block;
    width: 1200px;
    height: 627px;
  }
  .stripe-red { fill: var(--usa-red); }
  .canton { fill: var(--usa-blue); }
  .star { fill: var(--usa-white); }
  .badge-rim {
    fill: none;
    stroke: url(#rimGold);
    stroke-width: 6;
  }
  .heritage-title {
    font-family: "Days One", "Arial Black", sans-serif;
    text-anchor: middle;
    fill: url(#titleGold);
    stroke: var(--title-outline);
    stroke-width: 9;
    stroke-linejoin: round;
    paint-order: stroke fill;
  }
</style>
</head>
<body>
<svg class="board-top" viewBox="0 0 1200 627" xmlns="http://www.w3.org/2000/svg">
  <defs>
    <linearGradient id="rimGold" x1="0" y1="0" x2="1" y2="1">
      <stop offset="0" stop-color="var(--gold-light)"/>
      <stop offset="0.5" stop-color="var(--gold-mid)"/>
      <stop offset="1" stop-color="var(--gold-dark)"/>
    </linearGradient>
    <linearGradient id="titleGold" x1="0" y1="0" x2="0" y2="1">
      <stop offset="0" stop-color="var(--gold-light)"/>
      <stop offset="0.45" stop-color="var(--gold-mid)"/>
      <stop offset="0.6" stop-color="var(--gold-dark)"/>
      <stop offset="1" stop-color="var(--gold-light)"/>
    </linearGradient>
    <filter id="badgeShadow" x="-40%" y="-40%" width="200%" height="200%">
      <feDropShadow dx="10" dy="12" stdDeviation="7" flood-color="#000" flood-opacity="0.45"/>
    </filter>
    <filter id="titleShadow" x="-10%" y="-20%" width="130%" height="150%">
      <feDropShadow dx="5" dy="6" stdDeviation="4" flood-color="#000" flood-opacity="0.5"/>
    </filter>
    <clipPath id="badgeFace"><circle r="53"/></clipPath>
    <polygon id="star" points="0,-14 3.3,-4.5 13.3,-4.5 5.3,1.7 8.2,11.3 0,5.5 -8.2,11.3 -5.3,1.7 -13.3,-4.5 -3.3,-4.5"/>
  </defs>

  <!-- USA flag background -->
  <g class="usa-flag">
    <rect width="1200" height="627" fill="var(--usa-white)"/>
    <rect class="stripe-red" y="0" width="1200" height="48.23"/>
    <rect class="stripe-red" y="96.46" width="1200" height="48.23"/>
    <rect class="stripe-red" y="192.92" width="1200" height="48.23"/>
    <rect class="stripe-red" y="289.38" width="1200" height="48.23"/>
    <rect class="stripe-red" y="385.85" width="1200" height="48.23"/>
    <rect class="stripe-red" y="482.31" width="1200" height="48.23"/>
    <rect class="stripe-red" y="578.77" width="1200" height="48.23"/>
    <rect class="canton" width="480" height="337.6"/>
    <g class="stars">
      <use href="#star" class="star" x="40" y="27"/><use href="#star" class="star" x="120" y="27"/><use href="#star" class="star" x="200" y="27"/><use href="#star" class="star" x="280" y="27"/><use href="#star" class="star" x="360" y="27"/><use href="#star" class="star" x="440" y="27"/>
      <use href="#star" class="star" x="80" y="61.5"/><use href="#star" class="star" x="160" y="61.5"/><use href="#star" class="star" x="240" y="61.5"/><use href="#star" class="star" x="320" y="61.5"/><use href="#star" class="star" x="400" y="61.5"/>
      <use href="#star" class="star" x="40" y="96"/><use href="#star" class="star" x="120" y="96"/><use href="#star" class="star" x="200" y="96"/><use href="#star" class="star" x="280" y="96"/><use href="#star" class="star" x="360" y="96"/><use href="#star" class="star" x="440" y="96"/>
      <use href="#star" class="star" x="80" y="130.5"/><use href="#star" class="star" x="160" y="130.5"/><use href="#star" class="star" x="240" y="130.5"/><use href="#star" class="star" x="320" y="130.5"/><use href="#star" class="star" x="400" y="130.5"/>
      <use href="#star" class="star" x="40" y="165"/><use href="#star" class="star" x="120" y="165"/><use href="#star" class="star" x="200" y="165"/><use href="#star" class="star" x="280" y="165"/><use href="#star" class="star" x="360" y="165"/><use href="#star" class="star" x="440" y="165"/>
      <use href="#star" class="star" x="80" y="199.5"/><use href="#star" class="star" x="160" y="199.5"/><use href="#star" class="star" x="240" y="199.5"/><use href="#star" class="star" x="320" y="199.5"/><use href="#star" class="star" x="400" y="199.5"/>
      <use href="#star" class="star" x="40" y="234"/><use href="#star" class="star" x="120" y="234"/><use href="#star" class="star" x="200" y="234"/><use href="#star" class="star" x="280" y="234"/><use href="#star" class="star" x="360" y="234"/><use href="#star" class="star" x="440" y="234"/>
      <use href="#star" class="star" x="80" y="268.5"/><use href="#star" class="star" x="160" y="268.5"/><use href="#star" class="star" x="240" y="268.5"/><use href="#star" class="star" x="320" y="268.5"/><use href="#star" class="star" x="400" y="268.5"/>
      <use href="#star" class="star" x="40" y="303"/><use href="#star" class="star" x="120" y="303"/><use href="#star" class="star" x="200" y="303"/><use href="#star" class="star" x="280" y="303"/><use href="#star" class="star" x="360" y="303"/><use href="#star" class="star" x="440" y="303"/>
    </g>
  </g>

  <!-- Heritage flag badges -->
  <g class="badge badge-ireland" transform="translate(709 113)" filter="url(#badgeShadow)">
    <g clip-path="url(#badgeFace)">
      <rect x="-56" y="-56" width="38" height="112" fill="var(--ireland-green)"/>
      <rect x="-18" y="-56" width="36" height="112" fill="var(--usa-white)"/>
      <rect x="18" y="-56" width="38" height="112" fill="var(--ireland-orange)"/>
    </g>
    <circle class="badge-rim" r="53"/>
  </g>

  <g class="badge badge-italy" transform="translate(888 113)" filter="url(#badgeShadow)">
    <g clip-path="url(#badgeFace)">
      <rect x="-56" y="-56" width="38" height="112" fill="var(--italy-green)"/>
      <rect x="-18" y="-56" width="36" height="112" fill="var(--usa-white)"/>
      <rect x="18" y="-56" width="38" height="112" fill="var(--italy-red)"/>
      <circle r="13" fill="#b9c4b3" role="img" aria-label="Italian republic emblem"/>
    </g>
    <circle class="badge-rim" r="53"/>
  </g>

  <g class="badge badge-hungary" transform="translate(546 202)" filter="url(#badgeShadow)">
    <g clip-path="url(#badgeFace)">
      <rect x="-56" y="-56" width="112" height="38" fill="var(--hungary-red)"/>
      <rect x="-56" y="-18" width="112" height="36" fill="var(--usa-white)"/>
      <rect x="-56" y="18" width="112" height="38" fill="var(--hungary-green)"/>
      <rect x="-15" y="-35" width="30" height="62" rx="10" fill="#b8453f" role="img" aria-label="Hungarian coat of arms with crown"/>
    </g>
    <circle class="badge-rim" r="53"/>
  </g>

  <g class="badge badge-germany" transform="translate(1058 202)" filter="url(#badgeShadow)">
    <g clip-path="url(#badgeFace)">
      <rect x="-56" y="-56" width="112" height="38" fill="var(--germany-black)"/>
      <rect x="-56" y="-18" width="112" height="36" fill="var(--germany-red)"/>
      <rect x="-56" y="18" width="112" height="38" fill="var(--germany-gold)"/>
      <rect x="-17" y="-24" width="34" height="46" rx="8" fill="#d6a812" role="img" aria-label="German federal eagle shield"/>
    </g>
    <circle class="badge-rim" r="53"/>
  </g>

  <g class="badge badge-armenia" transform="translate(546 471)" filter="url(#badgeShadow)">
    <g clip-path="url(#badgeFace)">
      <rect x="-56" y="-56" width="112" height="38" fill="var(--armenia-red)"/>
      <rect x="-56" y="-18" width="112" height="36" fill="var(--armenia-blue)"/>
      <rect x="-56" y="18" width="112" height="38" fill="var(--armenia-orange)"/>
      <circle r="24" fill="var(--emblem-gold)" role="img" aria-label="Armenian coat of arms"/>
    </g>
    <circle class="badge-rim" r="53"/>
  </g>

  <g class="badge badge-russia" transform="translate(817 540)" filter="url(#badgeShadow)">
    <g clip-path="url(#badgeFace)">
      <rect x="-56" y="-56" width="112" height="38" fill="var(--usa-white)"/>
      <rect x="-56" y="-18" width="112" height="36" fill="var(--russia-blue)"/>
      <rect x="-56" y="18" width="112" height="38" fill="var(--russia-red)"/>
    </g>
    <circle class="badge-rim" r="53"/>
  </g>

  <g class="badge badge-moldova" transform="translate(1058 486)" filter="url(#badgeShadow)">
    <g clip-path="url(#badgeFace)">
      <rect x="-56" y="-56" width="38" height="112" fill="var(--moldova-blue)"/>
      <rect x="-18" y="-56" width="36" height="112" fill="var(--moldova-yellow)"/>
      <rect x="18" y="-56" width="38" height="112" fill="var(--moldova-red)"/>
      <rect x="-15" y="-22" width="30" height="42" rx="8" fill="var(--emblem-brown)" role="img" aria-label="Moldovan coat of arms with eagle"/>
    </g>
    <circle class="badge-rim" r="53"/>
  </g>

  <!-- Title -->
  <g class="heritage-title" filter="url(#titleShadow)">
    <text x="810" y="275" font-size="52" textLength="345" lengthAdjust="spacingAndGlyphs">WE PROUD</text>
    <text x="810" y="340" font-size="70" textLength="334" lengthAdjust="spacingAndGlyphs">OF OUR</text>
    <text x="810" y="398" font-size="56" textLength="368" lengthAdjust="spacingAndGlyphs">HERITAGE</text>
  </g>
</svg>
</body>
</html>
```